Maple Brook Concrete business card design

We need a business card developed for a local ready mix concrete company. We want a 2 sided design

The front just needs the basic contact info:

Raymond Vasquelli
P.555-014-2261
F. 555-014-2287
www.MapleBrookConcrete.Com
Raymond@MapleBrookConcrete.com
P.O Box 614
Succasunna, NJ, 07192

Service All of North And Central New Jersey With Ready Mix Concrete

The back will have a simple bullet point list:
• Metered Delivery - Use only what you pay for
• No Waste
• Multiple slumps on the fly
• No minimum delivery
• 24-7 service, all year
• No Hot Loads
• Fastest Service in the industry
Updates

I like the submissions using the existing colors. I think blue might also be a color to use as well. For the next trucks we order we will probably paint them blue. Colbalt blue

I must have made a typo: It should read, Serving all of North and Central New Jersey. It should also say: Pay for only what you use.

Target Market(s)

We will be targeting the construction industry

Industry/Entity Type

Concrete

Font styles to use
Serif
Sans Serif

Colors
ec2027

Requirements
Must have
• It needs to have a clean uncluttered look. The back is dedicated to telling customer what we do. Our advantage is we use a truck that delivers concrete with several advantages over barrel trucks, hence, why the back bullet points are important
Nice to have
• Our logo. I think since our logo is green, the front might look good with some red, like a red background (also the color of our truck)
Should not have
• clip art.

```html
<!DOCTYPE html>
<html lang="en">
<head>
<meta charset="utf-8">
<title>Maple Brook Concrete – Card Back</title>
<link href="https://fonts.googleapis.com/css2?family=Fira+Sans:wght@300;500&display=swap" rel="stylesheet">
<style>
  :root {
    --card-green: #a6cd3a;
    --ink: #141414;
    --accent-red: #c1113f;
  }
  html, body {
    margin: 0;
    padding: 0;
    width: 1200px;
    height: 686px;
    overflow: hidden;
  }
  .card-back {
    position: relative;
    width: 1200px;
    height: 686px;
    background: var(--card-green);
    font-family: "Fira Sans", Arial, sans-serif;
  }
  .advantages {
    position: absolute;
    left: 172px;
    top: 125px;
    margin: 0;
    padding: 0;
    list-style: none;
  }
  .advantage {
    position: relative;
    padding-left: 26px;
    font-size: 38px;
    line-height: 58px;
    font-weight: 300;
    color: var(--ink);
    white-space: nowrap;
  }
  .advantage::before {
    content: "";
    position: absolute;
    left: 3px;
    top: 27px;
    width: 6px;
    height: 6px;
    background: currentColor;
  }
  .advantage--highlight {
    font-weight: 500;
    color: var(--accent-red);
  }
</style>
</head>
<body>
  <main class="card-back">
    <ul class="advantages">
      <li class="advantage">No Waste</li>
      <li class="advantage">Multiple slumps on the fly</li>
      <li class="advantage">No minimum delivery</li>
      <li class="advantage">24-7 service, all year</li>
      <li class="advantage">No Hot Loads</li>
      <li class="advantage advantage--highlight">Fastest Service in the industry</li>
      <li class="advantage">Metered Delivery - Use only what you pay for</li>
    </ul>
  </main>
</body>
</html>
```